Website Redesign project for agency

we're looking to see some new designs for an agency website.
details in this google doc: https://files.brindlepath.example/sheet/d/7QXvRk2PaLw9HsNe4TyUc8JbZoMf3Gd61572-qKrA9w/view?mode=shared
homepage and one inner page/ or the blog page
please visit the google doc above to see the website that needs to be redesigned as well as an example website we like.
if you have any questions please send them to us asap
thank you
Target Market(s)
small business owners
Number of Pages Required
2 page
Font styles to use
Sans Serif
Requirements
Nice to have
- custom design
Should not have
- do not use a template you find online

```html
<!DOCTYPE html>
<html lang="en">
<head>
<meta charset="utf-8">
<title>Risewell Social — Agency Home</title>
<link href="https://fonts.googleapis.com/css2?family=Roboto:wght@300;400;500;700&display=swap" rel="stylesheet">
<style>
:root{
  --purple:#8a22e6;
  --purple-deep:#5f10d0;
  --pink:#ff2a7f;
  --ink:#1d1d24;
  --body:#3a3a44;
  --muted:#6d6d78;
  --line:#6a24e0;
  --grey:#ededee;
  --footer:#efefef;
  --white:#ffffff;
}
*{box-sizing:border-box;margin:0;padding:0}
html,body{width:1200px;height:3301px;overflow:hidden}
body{position:relative;background:var(--white);font-family:'Roboto',sans-serif;color:var(--ink)}
.abs{position:absolute}
a{color:inherit;text-decoration:none}

/* hero */
.hero-bg{position:absolute;left:0;top:0;width:1200px;height:600px}
.brand{position:absolute;font-weight:700;letter-spacing:1px;text-transform:uppercase}
.brand--head{left:190px;top:32px;font-size:26px;color:var(--white)}
.nav{position:absolute;top:38px;left:443px;display:flex;gap:0;font-size:15px;color:var(--white)}
.nav a{position:absolute;white-space:nowrap}
.btn{position:absolute;display:flex;align-items:center;justify-content:center;font-weight:500;border-radius:4px;font-size:15px}
.btn--pink{background:var(--pink);color:var(--white);box-shadow:0 8px 18px rgba(255,42,127,.3)}
.btn--ghost{border:1.5px solid rgba(255,255,255,.85);color:var(--white)}
.social-dot{position:absolute;left:82px;width:30px;height:30px;border:1.5px solid rgba(255,255,255,.85);border-radius:50%}
.social-dot::after{content:"";position:absolute;left:10px;top:10px;width:8px;height:8px;border-radius:50%;background:var(--white)}
.vertical-label{position:absolute;left:84px;top:440px;transform:rotate(-90deg);transform-origin:left top;font-size:12px;color:rgba(255,255,255,.8);white-space:nowrap}
.hero-title{position:absolute;left:187px;top:158px;color:var(--white);font-size:46px;line-height:54px}
.hero-title span{display:block}
.hero-title .light{font-weight:300}
.hero-title .bold{font-weight:700}
.hero-copy{position:absolute;left:187px;top:284px;width:400px;color:var(--white);font-size:17px;line-height:24px}
.scroll-hint{position:absolute;left:189px;top:480px;display:flex;align-items:center;gap:14px;color:var(--white);font-size:13px}
.mouse{width:12px;height:19px;border:1.5px solid var(--white);border-radius:6px;position:relative}
.mouse::after{content:"";position:absolute;left:4px;top:3px;width:1.5px;height:4px;background:var(--white)}
.hero-photo{position:absolute;left:640px;top:84px;width:500px;height:442px}

/* section heads */
.section-title{position:absolute;left:0;width:1200px;text-align:center;font-weight:500;font-size:36px}
.section-sub{position:absolute;left:0;width:1200px;text-align:center;font-size:15px;line-height:22px;color:var(--body)}

/* services */
.card{position:absolute;top:822px;width:260px;height:292px;background:var(--white);box-shadow:0 6px 26px rgba(0,0,0,.07);text-align:center}
.card__icon{position:absolute;left:79px;top:32px;width:102px;height:102px;border-radius:50%;background:var(--white);box-shadow:0 6px 22px rgba(0,0,0,.08)}
.card__glyph{position:absolute;left:30px;top:30px;width:42px;height:42px}
.card__title{position:absolute;top:158px;left:0;width:100%;font-size:19px;font-weight:500}
.card__text{position:absolute;top:194px;left:20px;width:220px;font-size:15px;line-height:23px;color:var(--body)}

/* about */
.about-photo{position:absolute;left:187px;top:1255px;width:402px;height:461px;border-radius:90px 0 110px 0;background:linear-gradient(135deg,#e9ecef 0%,#c9ced3 45%,#8a8f96 75%,#2c2f36 100%)}
.eyebrow{position:absolute;display:flex;align-items:center;gap:14px;color:var(--line);font-size:19px;font-weight:500}
.eyebrow::before{content:"";width:38px;height:2px;background:var(--line)}
.block-title{position:absolute;font-size:31px;line-height:38px;font-weight:400;color:var(--ink)}
.block-copy{position:absolute;font-size:15.5px;line-height:22.5px;color:var(--body)}

/* work showcase */
.showcase{position:absolute;left:173px;top:1786px;width:862px;height:420px;border-radius:6px;background:linear-gradient(180deg,#2a2a30 0%,#4b78b8 40%,#d9dce2 100%)}
.showcase-shadow{position:absolute;left:40px;top:2150px;width:1120px;height:40px;background:radial-gradient(ellipse at center,rgba(0,0,0,.08),rgba(0,0,0,0) 70%)}
.arrow{position:absolute;top:2036px;width:46px;height:46px;border-radius:50%;border:1.5px solid #e23a55;background:var(--white)}

/* testimonials */
.dots{position:absolute;left:489px;top:2380px;width:90px;height:90px}
.client-photo{position:absolute;left:197px;top:2424px;width:336px;height:387px;border-radius:0 0 50px 0;background:linear-gradient(160deg,#d8dde0 0%,#b9c3c6 45%,#6d93a6 100%)}
.quote-box{position:absolute;left:188px;top:2770px;width:57px;height:56px;background:var(--white);border-radius:4px;box-shadow:0 4px 16px rgba(0,0,0,.08)}
.client-name{position:absolute;left:612px;top:2672px;font-size:19px;font-weight:500}
.client-role{position:absolute;left:612px;top:2702px;font-size:14px;color:var(--body)}
.avatar{position:absolute;top:2740px;width:49px;height:49px;border-radius:50%}

/* footer */
.footer{position:absolute;left:0;top:2897px;width:1200px;height:404px;background:var(--footer)}
.brand--foot{left:187px;top:2974px;font-size:21px;color:var(--ink)}
.foot-copy{position:absolute;left:187px;top:3022px;width:270px;font-size:12.5px;line-height:22px;color:var(--body)}
.foot-social{position:absolute;top:3132px;width:12px;height:12px;border-radius:2px;background:var(--ink)}
.foot-head{position:absolute;top:2968px;font-size:14.5px;font-weight:500}
.foot-link{position:absolute;left:681px;font-size:12.5px;color:var(--body)}
.foot-contact{position:absolute;left:865px;font-size:12.5px;line-height:20px;color:var(--body)}
.foot-row{position:absolute;left:865px;display:flex;align-items:center;gap:14px;font-size:12.5px;color:var(--body)}
.rule{position:absolute;left:187px;top:3216px;width:832px;height:1px;background:#dadada}
.copyright{position:absolute;left:0;width:1200px;top:3250px;text-align:center;font-size:12.5px;color:var(--body)}
</style>
</head>
<body>

<!-- hero -->
<svg class="hero-bg" viewBox="0 0 1200 600" aria-hidden="true">
  <defs>
    <linearGradient id="heroGrad" x1="0" y1="0" x2="1" y2="1">
      <stop offset="0" stop-color="#9a2ae6"/>
      <stop offset="1" stop-color="#5a0fcf"/>
    </linearGradient>
  </defs>
  <rect x="0" y="0" width="1200" height="577" fill="var(--grey)"/>
  <path d="M0 0 H830 V300 C 800 480 720 598 560 598 H0 Z" fill="url(#heroGrad)"/>
</svg>

<div class="brand brand--head">Risewell Social</div>
<nav class="nav">
  <a style="left:0">What We Do</a>
  <a style="left:108px">Project</a>
  <a style="left:181px">Who We Are</a>
  <a style="left:288px">Book Us!</a>
</nav>
<a class="btn btn--pink" style="left:857px;top:26px;width:107px;height:46px">Login</a>

<span class="social-dot" style="top:184px"></span>
<span class="social-dot" style="top:234px"></span>
<span class="social-dot" style="top:284px"></span>
<span class="social-dot" style="top:334px"></span>
<div class="vertical-label" style="top:475px">Social Media</div>

<h1 class="hero-title"><span class="light">Lorem Ipsum is</span><span class="bold">simply dutmttmy text</span></h1>
<p class="hero-copy">A professionally designed website by Risewell Social makes your website attractive, functional, and mobile-friendly.</p>
<a class="btn btn--pink" style="left:187px;top:380px;width:160px;height:58px">Request Pricing</a>
<a class="btn btn--ghost" style="left:371px;top:380px;width:160px;height:58px">Our Work</a>
<div class="scroll-hint"><span class="mouse"></span>Keep Scrolling</div>

<svg class="hero-photo" viewBox="0 0 500 442" role="img" aria-label="Smiling man in a navy blazer holding an open laptop">
  <defs>
    <linearGradient id="manGrad" x1="0" y1="0" x2="0" y2="1">
      <stop offset="0" stop-color="#c9cbcf"/>
      <stop offset="1" stop-color="#2a3450"/>
    </linearGradient>
  </defs>
  <path d="M0 230 A 220 220 0 0 1 220 10 H 360 V 442 H 230 A 220 220 0 0 1 0 230 Z" fill="url(#manGrad)"/>
  <g fill="#c6b7e6">
    <circle cx="300" cy="18" r="2"/><circle cx="325" cy="18" r="2"/><circle cx="350" cy="18" r="2"/><circle cx="375" cy="18" r="2"/><circle cx="400" cy="18" r="2"/><circle cx="425" cy="18" r="2"/>
    <circle cx="375" cy="43" r="2"/><circle cx="400" cy="43" r="2"/><circle cx="425" cy="43" r="2"/>
    <circle cx="375" cy="68" r="2"/><circle cx="400" cy="68" r="2"/><circle cx="425" cy="68" r="2"/>
    <circle cx="375" cy="93" r="2"/><circle cx="400" cy="93" r="2"/><circle cx="425" cy="93" r="2"/>
    <circle cx="375" cy="118" r="2"/><circle cx="400" cy="118" r="2"/><circle cx="425" cy="118" r="2"/>
  </g>
  <path d="M340 390 L480 240 L500 250 L380 410 Z" fill="#b8babe"/>
</svg>

<!-- what we do -->
<h2 class="section-title" style="top:662px">What We Do</h2>
<p class="section-sub" style="top:722px">Lorem ipsum dolor sit amet, consectetur adipiscing elit, sed do eiusmod tempor<br>incididunt ut labore et dolore magna aliqua.</p>

<article class="card" style="left:187px">
  <div class="card__icon"><svg class="card__glyph" viewBox="0 0 42 42" aria-hidden="true"><circle cx="21" cy="21" r="13" fill="none" stroke="#5b4de0" stroke-width="2"/><rect x="17" y="10" width="8" height="22" rx="2" fill="#ff6fa6"/><circle cx="21" cy="21" r="4" fill="#5b4de0"/></svg></div>
  <h3 class="card__title">Web Design</h3>
  <p class="card__text">Lorem ipsum dolor sit amet, consectetur adipisicing elitsed do eiusmod tempor.</p>
</article>
<article class="card" style="left:471px">
  <div class="card__icon"><svg class="card__glyph" viewBox="0 0 42 42" aria-hidden="true"><circle cx="21" cy="17" r="12" fill="#e6e2ff" stroke="#5b4de0" stroke-width="2"/><rect x="9" y="12" width="24" height="6" rx="2" fill="#ff6fa6"/><rect x="19" y="29" width="4" height="11" rx="2" fill="#5b4de0"/></svg></div>
  <h3 class="card__title">SEO Services</h3>
  <p class="card__text">Lorem ipsum dolor sit amet, consectetur adipisicing elitsed do eiusmod tempor.</p>
</article>
<article class="card" style="left:752px">
  <div class="card__icon"><svg class="card__glyph" viewBox="0 0 42 42" aria-hidden="true"><rect x="5" y="7" width="32" height="28" rx="3" fill="#eef1ff" stroke="#5b4de0" stroke-width="2"/><rect x="5" y="7" width="32" height="6" fill="#c7cdfb"/><rect x="10" y="18" width="10" height="8" fill="#ff6fa6"/><rect x="23" y="18" width="9" height="2" fill="#5b4de0"/><rect x="23" y="23" width="9" height="2" fill="#5b4de0"/></svg></div>
  <h3 class="card__title">Social Media Marketing</h3>
  <p class="card__text">Lorem ipsum dolor sit amet, consectetur adipisicing elitsed do eiusmod tempor.</p>
</article>

<!-- about -->
<div class="about-photo" role="img" aria-label="Two colleagues writing on a whiteboard in a bright office"></div>
<div class="eyebrow" style="left:681px;top:1251px">About us</div>
<h2 class="block-title" style="left:681px;top:1297px;width:360px">We #1 Ranked Marketing agency</h2>
<p class="block-copy" style="left:681px;top:1388px;width:335px">Lorem ipsum dolor sit amet, consectetur adipisicing elit, sed do eiusmod tempor incididunt ut labore et dolore magna aliqua. Ut enim ad minim veniam, quis nostrud exercitation.</p>
<p class="block-copy" style="left:681px;top:1501px;width:335px">ullamco laboris nisi ut aliquip ex ea commodo consequat.</p>
<a class="btn btn--pink" style="left:681px;top:1571px;width:142px;height:50px">Read More</a>

<!-- work -->
<div class="showcase-shadow"></div>
<div class="showcase" role="img" aria-label="Client website shown on a desktop monitor, tablet and phone"></div>
<svg class="arrow" style="left:70px" viewBox="0 0 46 46" aria-hidden="true"><path d="M26 15 L18 23 L26 31" fill="none" stroke="#e23a55" stroke-width="2"/></svg>
<svg class="arrow" style="left:1083px" viewBox="0 0 46 46" aria-hidden="true"><path d="M20 15 L28 23 L20 31" fill="none" stroke="#e23a55" stroke-width="2"/></svg>
<a class="btn btn--pink" style="left:553px;top:2267px;width:190px;height:65px;font-size:15.5px">View More</a>

<!-- testimonials -->
<svg class="dots" viewBox="0 0 90 90" aria-hidden="true"><g fill="#bfe3dc">
  <circle cx="3" cy="3" r="3"/><circle cx="24" cy="3" r="3"/><circle cx="45" cy="3" r="3"/><circle cx="66" cy="3" r="3"/><circle cx="87" cy="3" r="3"/>
  <circle cx="3" cy="24" r="3"/><circle cx="24" cy="24" r="3"/><circle cx="45" cy="24" r="3"/><circle cx="66" cy="24" r="3"/><circle cx="87" cy="24" r="3"/>
  <circle cx="66" cy="45" r="3"/><circle cx="87" cy="45" r="3"/><circle cx="66" cy="66" r="3"/><circle cx="87" cy="66" r="3"/><circle cx="66" cy="87" r="3"/><circle cx="87" cy="87" r="3"/>
</g></svg>
<div class="client-photo" role="img" aria-label="Portrait of a young man in a teal shirt"></div>
<div class="quote-box"><svg viewBox="0 0 57 56" width="57" height="56" aria-hidden="true"><path d="M17 36 v-8 c0-6 3-10 8-11 l1 3 c-3 1-4 3-4 5 h4 v11 Z M31 36 v-8 c0-6 3-10 8-11 l1 3 c-3 1-4 3-4 5 h4 v11 Z" fill="var(--pink)"/></svg></div>

<div class="eyebrow" style="left:612px;top:2423px">Clients Love</div>
<h2 class="block-title" style="left:612px;top:2457px;font-weight:700;font-size:27px">Love from our Clients</h2>
<p class="block-copy" style="left:612px;top:2516px;width:395px;font-size:14px">Lorem ipsum dolor sit amet, consectetur adipisicing elit, sed do eiusmod tempor&nbsp; incididunt ut labore et dolore magna aliqua. Ut enim ad minim veniam, quis nostrud exercitation ullamco laboris nisi ut aliquip ex ea commodo consequat.uis aute irure dolor in reprehenderit in voluptate velit esse cillum dolore eu fugiat nulla pariatur.</p>
<div class="client-name">Milo Varenne</div>
<div class="client-role">Lorem ipsum</div>
<div class="avatar" style="left:612px;background:linear-gradient(135deg,#3ec6e0,#e04bb0)" role="img" aria-label="Client avatar"></div>
<div class="avatar" style="left:679px;background:linear-gradient(135deg,#d08a4a,#5a3420)" role="img" aria-label="Client avatar"></div>
<div class="avatar" style="left:749px;background:linear-gradient(135deg,#e6c07a,#2b2420)" role="img" aria-label="Client avatar"></div>

<!-- footer -->
<footer class="footer"></footer>
<div class="brand brand--foot">Risewell Social</div>
<p class="foot-copy">Lorem ipsum dolor sit amet, consectetur adipisicing elit, sed do eiusmod tempor incididunt ut labore et dolore magna aliqua. Ut enim ad minim.</p>
<span class="foot-social" style="left:188px"></span>
<span class="foot-social" style="left:219px"></span>
<span class="foot-social" style="left:253px"></span>
<span class="foot-social" style="left:287px"></span>

<h4 class="foot-head" style="left:681px">About Agency</h4>
<a class="foot-link" style="top:3030px">Home</a>
<a class="foot-link" style="top:3069px">About</a>
<a class="foot-link" style="top:3108px">Services</a>
<a class="foot-link" style="top:3147px">Contacts</a>

<h4 class="foot-head" style="left:863px;top:2966px">Contact Us</h4>
<p class="foot-contact" style="top:3030px;width:160px">Lorem ipsum dolor sit amet consecte.</p>
<div class="foot-row" style="top:3090px"><svg width="15" height="15" viewBox="0 0 16 16" aria-hidden="true"><path d="M4 1 L6.5 4 L5 6 C6 8.5 7.5 10 10 11 L12 9.5 L15 12 L13 15 C7 14.5 1.5 9 1 3 Z" fill="none" stroke="#555" stroke-width="1.1"/></svg>(01) 555-014-732</div>
<div class="foot-row" style="top:3124px"><svg width="15" height="12" viewBox="0 0 16 12" aria-hidden="true"><rect x="0.6" y="0.6" width="14.8" height="10.8" fill="none" stroke="#555" stroke-width="1.1"/><path d="M1 1 L8 7 L15 1" fill="none" stroke="#555" stroke-width="1.1"/></svg>lorem@mailbox.example</div>

<div class="rule"></div>
<p class="copyright">Copyright © 2020 RISEWELL SOCIAL. All rights reserved</p>

</body>
</html>
```